Post card

We need a post card design for a company Lorvi Academy. You can find more information about us on www.LorviAcademy-example.com.
The design should say about our Music, Art, Marquee Tots - Musical Theater, etc. classes. Classes are running after school hours.
Design should include our address and contact info.

Target Market(s)

Parents with kids 4-8

Requirements
Must have
• Short about after school/enrichment programs.
• Address/contact info.
• Must be fun.

```html
<!DOCTYPE html>
<html lang="en">
<head>
<meta charset="utf-8">
<title>Lorvi Academy – Postcard</title>
<link rel="stylesheet" href="https://fonts.googleapis.com/css2?family=Comfortaa:wght@500;700&family=Questrial&display=swap">
<style>
  :root {
    --page-bg: #f4f4f4;
    --sky-deep: #a9d3ea;
    --sky-mid: #bfe0ee;
    --sky-light: #e2f1f5;
    --panel-fill: rgba(240, 248, 250, 0.55);
    --panel-edge: rgba(255, 255, 255, 0.6);
    --headline: #d6f53a;
    --headline-glow: rgba(190, 245, 40, 0.75);
    --ink: #1a1a1a;
    --line: #111a0c;
    --line-glow: rgba(150, 230, 60, 0.7);
    --art-dark: #2b3a40;
  }
  html, body {
    margin: 0;
    width: 1200px;
    height: 900px;
    overflow: hidden;
    background: var(--page-bg);
  }
  .postcard {
    position: absolute;
    left: 60px;
    top: 90px;
    width: 1080px;
    height: 720px;
    overflow: hidden;
    background:
      radial-gradient(ellipse 620px 460px at 560px 250px, var(--sky-light) 0%, var(--sky-mid) 55%, var(--sky-deep) 100%);
    box-shadow: 0 6px 18px rgba(0, 0, 0, 0.25);
  }
  .headline {
    position: absolute;
    left: 24px;
    top: 110px;
    margin: 0;
    font-family: "Comfortaa", sans-serif;
    font-weight: 700;
    font-size: 40px;
    line-height: 48px;
    word-spacing: 10px;
    color: var(--headline);
    -webkit-text-stroke: 1px #9bc21a;
    text-shadow: 0 0 6px var(--headline-glow), 0 0 14px var(--headline-glow);
    z-index: 2;
  }
  .intro {
    position: absolute;
    left: 26px;
    top: 250px;
    margin: 0;
    font-family: "Questrial", sans-serif;
    font-size: 22px;
    line-height: 27px;
    color: var(--ink);
  }
  .artwork {
    position: absolute;
    left: 0;
    top: 355px;
    width: 172px;
    height: 365px;
    background: linear-gradient(180deg, rgba(43, 58, 64, 0) 0%, rgba(43, 58, 64, 0.35) 100%);
    border-top-right-radius: 80px;
  }
  .contact {
    position: absolute;
    left: 116px;
    top: 495px;
    font-family: "Questrial", sans-serif;
    color: var(--ink);
    letter-spacing: 2.5px;
  }
  .contact p { margin: 0; }
  .contact .name { font-size: 28px; line-height: 34px; }
  .contact .phone { font-size: 28px; line-height: 34px; font-weight: 700; -webkit-text-stroke: 0.6px var(--ink); }
  .contact .address { margin-top: 34px; font-size: 26px; line-height: 35px; }
  .contact .web { margin-top: 6px; font-size: 17px; font-weight: 700; -webkit-text-stroke: 0.4px var(--ink); }
  .mail-panel {
    position: absolute;
    left: 568px;
    top: 0;
    width: 501px;
    height: 720px;
    border-radius: 150px;
    background: linear-gradient(160deg, rgba(255, 255, 255, 0.6) 0%, var(--panel-fill) 45%, rgba(220, 238, 246, 0.4) 100%);
    box-shadow: inset 0 0 0 1px var(--panel-edge);
  }
  .address-lines {
    position: absolute;
    left: 50px;
    top: 476px;
    width: 409px;
  }
  .address-lines span {
    display: block;
    height: 3px;
    margin-bottom: 42px;
    background: var(--line);
    box-shadow: 0 0 4px var(--line-glow);
  }
</style>
</head>
<body>
  <main class="postcard">
    <div class="mail-panel">
      <div class="address-lines"><span></span><span></span><span></span><span></span></div>
    </div>
    <h1 class="headline">Jump into a world of<br>creativity at Lorvi Academy!</h1>
    <p class="intro">now offering after school enrichment<br>classes in music, art, marquee tots, &amp;<br>musical theater for toddlers and children!</p>
    <div class="artwork" role="img" aria-label="Decorative vine illustration with dancing child silhouettes and red and yellow butterflies"></div>
    <section class="contact">
      <p class="name">Lorvi Academy</p>
      <p class="phone">555-014-2273</p>
      <p class="address">48 Maple Row,<br>Eastfield, MA 01999</p>
      <p class="web">www.lorviacademy-example.com</p>
    </section>
  </main>
</body>
</html>
```